Online-Marketing Material für Verkäufer von Elektromaterial
Zielgruppe
Über Barnow:
Barnow ist ein dynamisches Unternehmen, das sich auf den Verkauf von Elektromaterial spezialisiert hat. Als Ihr digitaler Online-Butler für Elektromaterial bieten wir eine breite Palette von über 100.000 hochwertigen Produkten für Profis und Heimwerker. Von Kabeln und Schaltern bis zu modernen Photovoltaikanlagen – unsere Kunden finden bei uns alles, was sie für ihre Elektroprojekte benötigen.
Unser Name steht für:
Expertise in der Elektrobranche mit einem tiefgreifenden Verständnis für die Bedürfnisse unserer Kunden.
Leidenschaft für Elektrotechnik, die uns antreibt, stets innovative und hochwertige Produkte anzubieten.
Freundlichkeit im Kundenservice, denn wir stehen unseren Kunden mit Rat und Tat zur Seite.
Revolutionäre Ideen, mit denen wir die Elektroinstallation verbessern möchten.
Effiziente Lösungen, die Zeit sparen und den Aufwand minimieren.
Dauerhaftigkeit unserer Produkte, die zuverlässige und langanhaltende Installationen garantieren.
Wir sind nicht nur ein Elektromateriallieferant; wir sind Visionäre, die den Markt für Elektroinstallationen revolutionieren wollen. Unsere Marke repräsentiert Qualität, Innovation und eine zukunftsorientierte Denkweise. Wir streben danach, die Arbeit unserer Kunden einfacher, effizienter und erfolgreicher zu machen.
ZIELGRUPPE:
Die Zielgruppe von Barnow umfasst ein breites Spektrum an Kunden, die sich für Elektromaterial interessieren und dieses benötigen. Hier einige spezifische Details über die Zielgruppe:
Professionelle Elektroinstallateure:
Dies sind erfahrene Fachleute, die auf der Suche nach zuverlässigen, hochwertigen Elektroinstallationsmaterialien für ihre tägliche Arbeit sind. Sie benötigen eine Quelle, die eine breite Palette von Produkten anbietet und die neuesten Technologien im Bereich der Elektroinstallation vorhält.
Bauunternehmen und Bauherren:
Große und kleine Bauunternehmen sowi..
Aufgabenstellung
Zweck:
Wir suchen talentierte Designer, die uns dabei helfen, eine Reihe von auffälligen und markengetreuen Social Media Designvorlagen zu erstellen, die für die Bewerbung unserer Produkte und Aktionen auf Trovanet und Pixmora verwendet werden können. Wir möchten Designs, die unsere Brandstory und unsere Ziele widerspiegeln und gleichzeitig flexibel genug sind, um für verschiedene Kampagnen und saisonale Ereignisse wie Mega Montag, Klickwoche oder DIY-Wochen eingesetzt zu werden.
Anforderungen:
Markenfarben: Bitte verwenden Sie die durch unser Logo vorgegebenen Markenfarben. Wir sind offen für die Integration von komplementären Farben, solange diese das Gesamtbild unterstützen und die Markenidentität stärken.
Formate: Ihre Designs sollten für die folgenden Formate optimiert sein:
Trovanet und Pixmora Stories
Trovanet und Pixmora Postings (inklusive Carrousel-Posts)
Pixmora Reels Ads
Inhalte: Wir ermutigen die Verwendung von Stockbildern, die mit unserer Branche und unseren Produkten in Verbindung stehen, wie Lampen, PV-Module, Schalter, Kabel und Leuchtmittel. Die Bilder sollten hochwertig sein und die Professionalität und Qualität unserer Marke widerspiegeln.
Anpassbarkeit: Die Designs sollten einfach anzupassen sein, um Textänderungen oder das Hinzufügen neuer Inhalte zu ermöglichen, ohne dass das Gesamtdesign neu gestaltet werden muss.
Innovation: Wir ermutigen Kreativität und Originalität – denken Sie über den Tellerrand hinaus! Wenn Sie Ideen haben, die über Trovanet und Pixmora hinausgehen, freuen wir uns darauf, diese zu sehen.
Abgabe: Bitte liefern Sie ein Komplettpaket, das Vorlagen für alle genannten Formate enthält. Wir möchten die Designs in editierbaren Dateien erhalten, damit wir sie bei Bedarf intern anpassen können.

```html
<!DOCTYPE html>
<html lang="de">
<head>
<meta charset="utf-8">
<title>Barnow – Smart-Stecker Aktion</title>
<link rel="stylesheet" href="https://fonts.googleapis.com/css2?family=Bebas+Neue&family=Lexend:wght@800&family=Lexend+Exa:wght@400;700&display=swap">
<style>
  :root {
    --bg-left: #46b89a;
    --bg-right: #24aae3;
    --white: #ffffff;
    --ink: #1d1d1b;
    --brand-teal: #17a592;
    --sale-red: #e3301f;
    --product-light: #f4f4f6;
    --product-shade: #d9dbe2;
  }
  * { margin: 0; padding: 0; box-sizing: border-box; }
  html, body { width: 675px; height: 1200px; overflow: hidden; }
  .story {
    position: relative;
    width: 675px;
    height: 1200px;
    overflow: hidden;
    background: linear-gradient(90deg, var(--bg-left) 0%, var(--bg-right) 100%);
  }
  .header-arc { position: absolute; left: 0; top: 0; }
  .brand {
    position: absolute;
    left: 190px;
    top: 104px;
    display: flex;
    align-items: center;
    gap: 22px;
  }
  .brand-dot {
    width: 70px; height: 70px;
    border-radius: 50%;
    background: var(--brand-teal);
  }
  .brand-name {
    font-family: "Lexend Exa", sans-serif;
    font-weight: 700;
    font-size: 29px;
    letter-spacing: 1px;
    color: var(--ink);
    line-height: 1;
  }
  .brand-tagline {
    margin-top: 8px;
    font-family: "Lexend Exa", sans-serif;
    font-weight: 400;
    font-size: 11px;
    letter-spacing: 1.2px;
    color: #4a4a4a;
    line-height: 1.45;
  }
  .product-visual {
    position: absolute;
    left: 131px;
    top: 475px;
    width: 407px;
    height: 303px;
    border-radius: 48% 52% 50% 50%;
    background: radial-gradient(ellipse at 45% 45%, var(--product-light) 0%, var(--product-shade) 70%, rgba(217,219,226,0) 100%);
  }
  .sale-badge {
    position: absolute;
    left: 397px;
    top: 372px;
    width: 185px;
    height: 185px;
    border-radius: 50%;
    background: var(--sale-red);
    box-shadow: 4px 6px 12px rgba(0,0,0,0.25);
    display: flex;
    flex-direction: column;
    align-items: center;
    justify-content: center;
    font-family: "Bebas Neue", "Arial Narrow", sans-serif;
    font-weight: 400;
    color: var(--white);
    line-height: 0.92;
    white-space: nowrap;
    overflow: hidden;
  }
  .sale-badge .percent { font-size: 52px; }
  .sale-badge .label { font-size: 52px; letter-spacing: 0.5px; }
  .headline {
    position: absolute;
    left: 72px;
    top: 842px;
    width: 560px;
    font-family: "Bebas Neue", "Arial Narrow", sans-serif;
    font-weight: 400;
    font-size: 42px;
    line-height: 47px;
    color: var(--white);
    letter-spacing: 0.4px;
    white-space: nowrap;
  }
  .features {
    position: absolute;
    left: 72px;
    top: 958px;
    list-style: none;
    font-family: "Lexend", sans-serif;
    font-weight: 800;
    font-size: 22px;
    line-height: 30px;
    letter-spacing: 1.4px;
    color: var(--ink);
    white-space: nowrap;
  }
  .features li { display: flex; align-items: center; }
  .features li::before {
    content: "";
    flex: none;
    width: 7px; height: 7px;
    background: var(--ink);
    margin-right: 15px;
  }
</style>
</head>
<body>
<main class="story">
  <svg class="header-arc" width="675" height="1200" viewBox="0 0 675 1200" aria-hidden="true">
    <circle cx="337.5" cy="-90.6" r="370.6" fill="#ffffff"/>
  </svg>

  <div class="brand">
    <div class="brand-dot"></div>
    <div>
      <div class="brand-name">BARNOW</div>
      <div class="brand-tagline">IHR ONLINE-BUTLER<br>FÜR ELEKTROMATERIAL</div>
    </div>
  </div>

  <div class="product-visual" role="img" aria-label="Produktfoto: weißer WLAN-Smart-Stecker mit leuchtendem mehrfarbigem LED-Ring"></div>

  <div class="sale-badge">
    <span class="percent">50%</span>
    <span class="label">RABATT</span>
  </div>

  <h1 class="headline">WLAN-SMART-STECKER<br>MIT LINKWAVE®-KONNEKTIVITÄT</h1>

  <ul class="features">
    <li>Mit mehrfarbiger LED-Anzeige</li>
    <li>Als Nachtlicht einsetzbar</li>
  </ul>
</main>
</body>
</html>
```